Create a flyer that will catch your eye and make you want to call us for KELVOTH seamless Gutters

We are looking for a logo to help us with sales of our seamless gutter business, we are looking to expand, add loyal customers and increase our referral business.
We provide a turn key process from sales to install. we show up with our rolling factory, our truck spits out what seems to be an endless supply of gutter!
Each job is fabricated and installed to meet your homes design.

Target Market(s)

Treasure Coast of Florida, single story Homes

Font styles to use
Serif

Requirements
Must have
• Our Logo and Name on the flyer
Clean design with a clear message
call to action

```html
<!DOCTYPE html>
<html lang="en">
<head>
<meta charset="utf-8">
<title>Kelvoth Gutters – Seamless Gutter System Flyer</title>
<link rel="stylesheet" href="https://fonts.googleapis.com/css2?family=Montserrat:wght@300;400;500;600;700;800&display=swap">
<style>
  :root {
    --green: #13994a;
    --green-dark: #0d7a3a;
    --grey-band: #b3b3b3;
    --charcoal: #3a3a3a;
    --ink: #2b2b2b;
    --text-grey: #555555;
    --gold-light: #f3d36b;
    --gold-dark: #c4951d;
    --white: #ffffff;
    --sky: #dfe9f2;
    --sky-deep: #9fbcd6;
  }
  * { box-sizing: border-box; margin: 0; padding: 0; }
  html, body { width: 900px; height: 1200px; overflow: hidden; background: var(--white); }
  body { font-family: "Montserrat", sans-serif; color: var(--ink); }

  .flyer { position: relative; width: 900px; height: 1200px; background: var(--white); overflow: hidden; }

  /* Brand */
  .brand { position: absolute; left: 30px; top: 60px; display: flex; align-items: center; gap: 16px; }
  .brand-dot { width: 58px; height: 58px; border-radius: 50%; background: var(--green); }
  .brand-name { font-size: 46px; font-weight: 800; color: var(--green); letter-spacing: -1px; }
  .website { position: absolute; right: 34px; top: 52px; font-size: 22px; font-weight: 700; color: var(--text-grey); }

  /* Photo areas */
  .photo-main { position: absolute; left: 430px; top: 100px; width: 470px; height: 560px;
    clip-path: polygon(120px 0, 470px 0, 470px 560px, 0 560px, 30px 330px);
    background: linear-gradient(160deg, var(--sky) 0%, #f4f6f8 45%, #cfd6dc 100%); }
  .photo-small { position: absolute; top: 486px; width: 224px; height: 166px; border: 6px solid var(--white);
    box-shadow: 0 2px 6px rgba(0,0,0,.15); }
  .photo-small.downspout { left: 396px; background: linear-gradient(180deg, #c9d3dc, #eef2f5); }
  .photo-small.roof-edge { left: 634px; background: linear-gradient(160deg, #b86a3c 0%, #e8e2d6 50%, var(--sky-deep) 100%); }

  /* Headline panel */
  .headline-panel { position: absolute; left: 0; top: 226px; width: 400px; height: 274px; background: var(--green);
    clip-path: polygon(0 0, 400px 0, 325px 274px, 0 274px); color: var(--white); padding: 22px 0 0 32px; }
  .headline-panel .thin { font-size: 48px; font-weight: 300; line-height: 1; letter-spacing: 1px; }
  .headline-panel .bold { font-size: 56px; font-weight: 700; line-height: 1.02; }
  .headline-panel .tagline { margin-top: 16px; font-size: 18px; font-weight: 600; line-height: 1.2; width: 270px; }

  .intro { position: absolute; left: 30px; top: 526px; width: 320px; font-size: 13.5px; line-height: 1.42;
    text-align: justify; color: var(--text-grey); }

  /* Grey band with badges */
  .service-band { position: absolute; left: 0; top: 697px; width: 900px; height: 151px; background: var(--grey-band); }
  .service-band .note { position: absolute; left: 548px; top: 22px; width: 310px; color: var(--white);
    font-size: 17px; font-weight: 500; line-height: 1.36; }

  .badge { position: absolute; top: 668px; width: 212px; height: 212px; }
  .badge.warranty { left: 32px; }
  .badge.free { left: 288px; }
  .badge-text { position: absolute; inset: 0; display: flex; flex-direction: column; align-items: center;
    text-align: center; padding-top: 50px; }
  .badge-text .pre { font-size: 11px; font-weight: 700; color: var(--ink); }
  .badge-text .ribbon { margin-top: 6px; width: 226px; background: var(--green); color: var(--white);
    font-weight: 800; line-height: 1; padding: 6px 0; }
  .badge.warranty .ribbon { font-size: 21px; line-height: .95; }
  .badge.free .ribbon { font-size: 38px; }
  .badge-text .detail { margin-top: 7px; width: 120px; font-size: 10px; line-height: 1.2; color: var(--text-grey); }

  /* Process statement */
  .process { position: absolute; right: 48px; top: 882px; width: 640px; text-align: right; font-size: 19px;
    font-weight: 500; line-height: 1.32; color: var(--ink); }
  .process-rule { position: absolute; left: 855px; top: 884px; width: 5px; height: 68px; background: var(--green); }

  .technician { position: absolute; left: 12px; top: 895px; width: 238px; height: 305px;
    background: linear-gradient(180deg, #e8edf3 0%, #2f5fb8 55%, #1f4793 100%); }
  .megaphone { position: absolute; left: 274px; top: 978px; width: 200px; height: 114px;
    background: linear-gradient(135deg, #eeeeee, #cfd8cf); }

  .referral { position: absolute; left: 523px; top: 981px; width: 344px; height: 118px; background: var(--charcoal);
    border-radius: 10px 10px 0 0; color: var(--white); text-align: center; padding-top: 10px; }
  .referral .offer { font-size: 50px; font-weight: 700; line-height: 1; }
  .referral .offer sup { font-size: 26px; vertical-align: 18px; }
  .referral .label { font-size: 38px; font-weight: 400; line-height: 1.15; }

  /* Contact bar */
  .contact-bar { position: absolute; left: 0; top: 1098px; width: 900px; height: 102px; background: var(--green); color: var(--white); }
  .call { position: absolute; left: 304px; top: 12px; }
  .call .cta { font-size: 30px; font-weight: 700; line-height: 1.1; }
  .call .phone { font-size: 36px; font-weight: 700; display: flex; align-items: center; gap: 10px; }
  .details { position: absolute; left: 666px; top: 14px; font-size: 13px; font-weight: 500; line-height: 1.3; }
  .details .row { display: flex; gap: 8px; align-items: flex-start; }
  .details .office { margin-top: 10px; font-size: 20px; font-weight: 600; align-items: center; }
  .icon { fill: var(--white); flex: none; }
</style>
</head>
<body>
<main class="flyer">
  <div class="brand">
    <span class="brand-dot"></span>
    <span class="brand-name">Kelvoth Gutters</span>
  </div>
  <div class="website">www.kelvothgutters.com</div>

  <div class="photo-main" role="img" aria-label="Photo looking up at a seamless white gutter and downspout on a house eave against the sky"></div>
  <div class="photo-small downspout" role="img" aria-label="Photo of a white downspout on a house corner"></div>
  <div class="photo-small roof-edge" role="img" aria-label="Photo of a tiled roof edge with a gutter"></div>

  <section class="headline-panel">
    <div class="thin">SEAMLESS</div>
    <div class="bold">GUTTER<br>SYSTEM</div>
    <p class="tagline">Each job is fabricated and installed to meet your homes design</p>
  </section>

  <p class="intro">Kelvoth Gutters provides top quality seamless gutter system that will protect your home for many years. Our traveling gutter factory on wheels allows us to custom fit gutters to your homes specific needs at a competitive price. We take pride in our excellent customer service, professional installs and quality products.</p>

  <section class="service-band">
    <p class="note">Someone is always available to answer your calls, provide answers to your questions and update you on the progress of your job.</p>
  </section>

  <div class="badge warranty">
    <svg width="212" height="212" viewBox="0 0 212 212" aria-hidden="true">
      <defs><linearGradient id="gold1" x1="0" y1="0" x2="1" y2="1"><stop offset="0" stop-color="#f3d36b"/><stop offset="1" stop-color="#c4951d"/></linearGradient></defs>
      <circle cx="106" cy="106" r="104" fill="url(#gold1)"/>
      <circle cx="106" cy="106" r="88" fill="#ffffff"/>
    </svg>
    <div class="badge-text">
      <span class="pre">WE PROVIDE</span>
      <span class="ribbon">VERY BEST<br>WARRANTY</span>
      <span class="detail">in the business and use the best materials available</span>
    </div>
  </div>

  <div class="badge free">
    <svg width="212" height="212" viewBox="0 0 212 212" aria-hidden="true">
      <defs><linearGradient id="gold2" x1="0" y1="0" x2="1" y2="1"><stop offset="0" stop-color="#f3d36b"/><stop offset="1" stop-color="#c4951d"/></linearGradient></defs>
      <circle cx="106" cy="106" r="104" fill="url(#gold2)"/>
      <circle cx="106" cy="106" r="88" fill="#ffffff"/>
    </svg>
    <div class="badge-text">
      <span class="pre">WE PROVIDE</span>
      <span class="ribbon">FREE</span>
      <span class="detail">in home estimates and are adhering to stringent covid-19 protocols</span>
    </div>
  </div>

  <p class="process">We provide a turn key process from sales to install. we show up with our rolling factory, our truck spits out what seems to be an endless supply of gutter!</p>
  <div class="process-rule"></div>

  <div class="technician" role="img" aria-label="Photo of a smiling gutter technician in a blue cap and blue work shirt with arms crossed"></div>
  <div class="megaphone" role="img" aria-label="Illustration of a megaphone with green sound marks"></div>

  <div class="referral">
    <div class="offer">Get a <sup>$</sup>100</div>
    <div class="label">Referral fee</div>
  </div>

  <footer class="contact-bar">
    <div class="call">
      <div class="cta">Call us today!</div>
      <div class="phone">
        <svg class="icon" width="26" height="26" viewBox="0 0 24 24" aria-hidden="true"><path d="M6.6 10.8a15.1 15.1 0 0 0 6.6 6.6l2.2-2.2c.3-.3.7-.4 1-.2 1.1.4 2.3.6 3.6.6.6 0 1 .4 1 1V20c0 .6-.4 1-1 1C10.6 21 3 13.4 3 4c0-.6.4-1 1-1h3.5c.6 0 1 .4 1 1 0 1.3.2 2.5.6 3.6.1.3 0 .7-.2 1z"/></svg>
        555-014-2280
      </div>
    </div>
    <div class="details">
      <div class="row">
        <svg class="icon" width="12" height="16" viewBox="0 0 12 16" aria-hidden="true"><path d="M6 0a6 6 0 0 0-6 6c0 4.5 6 10 6 10s6-5.5 6-10a6 6 0 0 0-6-6zm0 8.2A2.2 2.2 0 1 1 6 3.8a2.2 2.2 0 0 1 0 4.4z"/></svg>
        <span>120 Harbor Lane<br>Seabrook, Florida 30000</span>
      </div>
      <div class="row office">
        <svg class="icon" width="16" height="16" viewBox="0 0 24 24" aria-hidden="true"><path d="M6.6 10.8a15.1 15.1 0 0 0 6.6 6.6l2.2-2.2c.3-.3.7-.4 1-.2 1.1.4 2.3.6 3.6.6.6 0 1 .4 1 1V20c0 .6-.4 1-1 1C10.6 21 3 13.4 3 4c0-.6.4-1 1-1h3.5c.6 0 1 .4 1 1 0 1.3.2 2.5.6 3.6.1.3 0 .7-.2 1z"/></svg>
        <span>555-014-3391</span>
      </div>
    </div>
  </footer>
</main>
</body>
</html>
```